Brantley Advisory Group provides support for renewable energy projects to utilities and suppliers

I need a professional looking business card that is both simple and elegant and unique. My clients are mostly large organizations not individuals. I am a consultant with my own company that is small but would like to give clients the impression I am larger. Smart grid, fiber optics, software, field hardware, distribution automation, substation automation, operations, energy storage/batteries, microgrids, customer service, strategy/roadmaps, conservation, Automated Metering Infrastruture (AMI or smart meters) are all areas of focus.

Target Market(s)

Utilities, suppliers, governmental agencies involved in energy. All types of energy especially natural gas and electrical. Especially renewable energy or green projects.

Contact Information for Business Card

Name - Mark Brantley Cell Phone - 425.318.2746 Email - mbrantley@brantleyag-example.com
Company - Brantley Advisory Group (logo) Title - Principal

Font styles to use
Serif
Sans Serif

Colors

Designer to choose colors to be used in the design.

Requirements
Must have
• Simple and professional and powerful.
• Unique/creative design.
Nice to have
• Utilize color scheme to accent logo colors. Maybe some geometric pattern on edge of card with color.
Should not have
• Busy, complicated, traditional

```html
<!DOCTYPE html>
<html lang="en">
<head>
<meta charset="utf-8">
<title>Brantley Advisory Group – Business Card</title>
<link href="https://fonts.googleapis.com/css2?family=Lato:wght@700;900&display=swap" rel="stylesheet">
<style>
  :root {
    --canvas: #d1d2d4;
    --paper: #ffffff;
    --brand-blue: #1d3f95;
    --deep-blue: #050f45;
    --brand-green: #658a3c;
  }
  * { margin: 0; padding: 0; box-sizing: border-box; }
  html, body { width: 984px; height: 1200px; overflow: hidden; background: var(--canvas); }
  body { position: relative; font-family: "Lato", Arial, sans-serif; }

  .card { position: absolute; left: 33px; width: 913px; height: 547px; overflow: hidden; }
  .card--front { top: 34px; background: var(--paper); }
  .card--back { top: 615px; background: var(--brand-blue); }

  .rule { position: absolute; height: 8px; }
  .rule--left { left: 0; width: 248px; top: 118px; }
  .rule--right { right: 0; width: 247px; top: 200px; }
  .card--front .rule--left { background: var(--brand-green); }
  .card--front .rule--right { background: var(--brand-blue); }
  .card--back .rule { background: var(--paper); }
  .card--back .rule--left { top: 216px; }
  .card--back .rule--right { top: 301px; }

  .wordmark { position: absolute; left: 253px; top: 96px; display: flex; align-items: center; gap: 26px; }
  .card--back .wordmark { top: 200px; }
  .wordmark__square { width: 88px; height: 88px; border: 6px solid currentColor; border-radius: 6px; }
  .wordmark__name { font-weight: 900; line-height: 1; }
  .wordmark__name span { display: block; }
  .wordmark__top { font-size: 62px; letter-spacing: -0.5px; }
  .wordmark__bottom { font-size: 35px; margin-top: 6px; }
  .card--front .wordmark { color: var(--brand-blue); }
  .card--back .wordmark { color: var(--paper); }

  .identity { position: absolute; top: 258px; left: 0; width: 100%; height: 72px; }
  .identity__name {
    position: absolute; right: 418px; top: 14px;
    font-size: 42px; font-weight: 900; color: var(--brand-green); white-space: nowrap; letter-spacing: 0.5px;
  }
  .identity__divider { position: absolute; left: 505px; top: 0; width: 2px; height: 71px; background: var(--brand-blue); }
  .identity__title {
    position: absolute; left: 529px; top: 24px;
    font-size: 29px; font-weight: 900; color: var(--brand-blue); letter-spacing: 0.5px;
  }

  .band { position: absolute; left: 0; width: 913px; }
  .band--contact { top: 353px; height: 194px; }
  .band--footer { bottom: 0; height: 96px; }
  .band svg { display: block; }

  .contact { position: absolute; display: flex; align-items: center; color: var(--paper); font-weight: 700; white-space: nowrap; }
  .contact__icon {
    width: 72px; height: 72px; border-radius: 50%; background: var(--paper);
    display: flex; align-items: center; justify-content: center; flex: none;
  }
  .contact--phone { left: 75px; top: 443px; top: 78px; }
  .contact--phone .contact__text { font-size: 30px; margin-left: 23px; letter-spacing: 0.5px; }
  .contact--email { left: 444px; top: 78px; }
  .contact--email .contact__text { font-size: 21px; margin-left: 28px; }
</style>
</head>
<body>

<section class="card card--front">
  <div class="rule rule--left"></div>
  <div class="rule rule--right"></div>

  <div class="wordmark">
    <div class="wordmark__square"></div>
    <div class="wordmark__name"><span class="wordmark__top">Brantley</span><span class="wordmark__bottom">Advisory Group</span></div>
  </div>

  <div class="identity">
    <div class="identity__name">MARK BRANTLEY</div>
    <div class="identity__divider"></div>
    <div class="identity__title">PRINCIPAL</div>
  </div>

  <div class="band band--contact">
    <svg width="913" height="194" viewBox="0 0 913 194">
      <defs>
        <linearGradient id="contactShade" x1="250" y1="110" x2="430" y2="60" gradientUnits="userSpaceOnUse">
          <stop offset="0" stop-color="#1d3f95"/>
          <stop offset="0.5" stop-color="#1d3f95"/>
          <stop offset="1" stop-color="#050f45"/>
        </linearGradient>
      </defs>
      <rect width="913" height="194" fill="url(#contactShade)"/>
      <polygon points="360,0 913,0 913,194 478,194" fill="#658a3c"/>
    </svg>

    <div class="contact contact--phone">
      <div class="contact__icon">
        <svg width="34" height="44" viewBox="0 0 34 44">
          <rect x="6" y="4" width="20" height="36" rx="3" transform="rotate(-12 16 22)" fill="none" stroke="#658a3c" stroke-width="3.5"/>
          <circle cx="20" cy="35" r="1.8" fill="#658a3c"/>
        </svg>
      </div>
      <span class="contact__text">425.318.2746</span>
    </div>

    <div class="contact contact--email">
      <div class="contact__icon">
        <svg width="44" height="38" viewBox="0 0 44 38">
          <polygon points="4,20 18,4 40,14 24,34" fill="#1d3f95"/>
          <polyline points="4,20 22,22 40,14" fill="none" stroke="#ffffff" stroke-width="2.5"/>
        </svg>
      </div>
      <span class="contact__text">mbrantley@brantleyag-example.com</span>
    </div>
  </div>
</section>

<section class="card card--back">
  <div class="rule rule--left"></div>
  <div class="rule rule--right"></div>

  <div class="wordmark">
    <div class="wordmark__square"></div>
    <div class="wordmark__name"><span class="wordmark__top">Brantley</span><span class="wordmark__bottom">Advisory Group</span></div>
  </div>

  <div class="band band--footer">
    <svg width="913" height="96" viewBox="0 0 913 96">
      <defs>
        <linearGradient id="footerShade" x1="260" y1="70" x2="410" y2="20" gradientUnits="userSpaceOnUse">
          <stop offset="0" stop-color="#1d3f95"/>
          <stop offset="0.45" stop-color="#1d3f95"/>
          <stop offset="1" stop-color="#050f45"/>
        </linearGradient>
      </defs>
      <rect width="913" height="96" fill="url(#footerShade)"/>
      <polygon points="360,0 913,0 913,96 418,96" fill="#658a3c"/>
    </svg>
  </div>
</section>

</body>
</html>
```